We need a corporate look website for our Company (Beit Karim for Bright Works) in Oman. We are doing Cabling Supply & Service, BMS SUpply ANd service, Fire and safety supply & Service, Video wall system supply and service, CCTV, Access control, Bio metric system, IT Software and Hardware Supply.
I will give some companies website which are doing the same business, Please refer below.
Cabling service- http://www.veltro-cablenet.com/
BMS , Video wall system, Fire and safety- http://www.qirantechgulf.com/
https://www.pqv-gl.com/
https://www.alwardasystems.com/

i have uploaded pour company letter head also. Please do the design with the same color in our logo.

```html
<!DOCTYPE html>
<html lang="en">
<head>
<meta charset="utf-8">
<title>Beit Karim for Bright Works</title>
<link rel="stylesheet" href="https://fonts.googleapis.com/css2?family=Roboto:wght@400;500;700;900&family=Open+Sans:wght@400;600&display=swap">
<style>
:root{
  --red:#c8161d;
  --red-dark:#9e0f15;
  --navy:#1d1f35;
  --navy-deep:#161829;
  --ink:#1b1b1b;
  --text:#555a60;
  --light:#eef0f2;
  --white:#ffffff;
  --line:#d9dcdf;
}
*{box-sizing:border-box;margin:0;padding:0}
html,body{width:1200px;height:4444px;overflow:hidden;background:var(--white)}
body{font-family:"Open Sans",sans-serif;color:var(--text);position:relative}
.page{position:relative;width:1200px;height:4444px;overflow:hidden}
.abs{position:absolute}

/* header */
.hero{position:absolute;left:0;top:0;width:1200px;height:780px}
.hero-photo{position:absolute;inset:0;width:1200px;height:780px}
.topbar{position:absolute;top:0;left:0;width:1200px;height:38px}
.topbar-info{position:absolute;top:0;left:530px;height:36px;display:flex;align-items:center;gap:34px;font:500 15px "Roboto",sans-serif;color:var(--white)}
.topbar-info span{display:flex;align-items:center;gap:10px}
.socials{display:flex;gap:6px}
.socials i{display:block;width:18px;height:18px;border:1.5px solid var(--white);border-radius:50%}
.logo{position:absolute;left:127px;top:8px;width:126px;text-align:center}
.logo-mark{width:126px;height:126px;background:var(--red);display:block}
.logo-name{display:block;margin-top:12px;font:500 20px "Roboto",sans-serif;color:var(--white);letter-spacing:1px}
.nav{position:absolute;top:78px;left:444px;display:flex;gap:26px;font:500 16px "Roboto",sans-serif;color:var(--white)}
.hero-title{position:absolute;right:140px;top:222px;text-align:right;font:700 50px/1.18 "Roboto",sans-serif;color:var(--white)}
.hero-sub{position:absolute;right:140px;top:356px;text-align:right;font:400 17px/1.6 "Open Sans",sans-serif;color:var(--white)}
.btn-red{position:absolute;left:868px;top:436px;width:194px;height:46px;border-radius:23px;background:var(--red);color:var(--white);font:700 16px "Roboto",sans-serif;display:flex;align-items:center;justify-content:center}
.dots{position:absolute;top:688px;left:560px;display:flex;gap:10px;align-items:center}
.dots i{width:12px;height:12px;border-radius:50%;background:var(--white);display:block}
.dots i.on{width:18px;height:18px;border:3px solid var(--white);background:transparent}

/* headings */
.section-title{position:absolute;left:0;width:1200px;text-align:center;font:400 40px "Roboto",sans-serif;color:var(--ink);letter-spacing:1px}
.section-title b{font-weight:700}
.rule{position:absolute;left:562px;width:76px;height:4px;background:var(--red)}

/* services */
.service{position:absolute;width:300px;text-align:center}
.service-icon{display:block;margin:0 auto}
.service h3{margin-top:22px;font:700 17px "Roboto",sans-serif;color:var(--ink)}
.service p{margin-top:14px;font:400 14px/1.9 "Open Sans",sans-serif;color:var(--text)}

/* band */
.band{position:absolute;left:0;top:1618px;width:1200px;height:436px}
.band-label{position:absolute;font:700 26px/1.3 "Roboto",sans-serif;color:var(--white);text-align:center;width:320px}

/* welcome */
.welcome{position:absolute;left:0;top:2054px;width:1200px;height:576px;background:var(--light)}
.welcome-photo{position:absolute;left:560px;top:0;width:640px;height:576px}
.welcome h2{position:absolute;left:154px;top:96px;font:700 40px "Roboto",sans-serif;color:var(--ink)}
.welcome h2 span{color:var(--red);font-weight:400}
.welcome p{position:absolute;left:154px;top:168px;width:440px;font:400 14px/1.95 "Open Sans",sans-serif;color:var(--text)}
.btn-outline{position:absolute;left:154px;top:392px;width:120px;height:36px;border:2px solid var(--ink);font:500 14px "Roboto",sans-serif;color:var(--ink);display:flex;align-items:center;justify-content:center}

/* news */
.news-card{position:absolute;width:288px;height:358px;background:var(--white);box-shadow:0 2px 10px rgba(0,0,0,.14)}
.news-photo{display:block;width:288px;height:184px}
.news-card h4{margin:22px 18px 0;font:500 19px "Roboto",sans-serif;color:var(--ink)}
.news-date{margin:14px 18px 0;display:flex;align-items:center;gap:8px;font:700 12px "Roboto",sans-serif;color:var(--red);letter-spacing:.5px}
.news-card p{margin:12px 18px 0;font:400 13px/1.75 "Open Sans",sans-serif;color:var(--text)}

/* testimonials */
.testimonials{position:absolute;left:0;top:3318px;width:1200px;height:730px}
.testimonials .section-title{color:var(--white);top:56px;font-weight:700}
.quote-card{position:absolute;top:208px;width:404px;height:208px;background:var(--white);border-radius:4px;padding:28px 26px}
.quote-card p{font:400 13px/1.8 "Open Sans",sans-serif;color:var(--text)}
.quote-name{position:absolute;bottom:28px;font:500 17px/1.55 "Roboto",sans-serif;color:var(--red)}
.quote-mark{position:absolute;bottom:36px;font:900 56px/1 "Roboto",sans-serif;color:#9a9a9a}
.avatar{position:absolute;top:3646px;width:118px;height:118px;border-radius:50%;border:5px solid var(--white);background:linear-gradient(160deg,#b9b4ad,#6e6862)}

/* footer */
.footer-title{position:absolute;top:4012px;font:700 22px "Roboto",sans-serif;color:var(--white)}
.contact-list{position:absolute;left:172px;top:4074px;list-style:none;font:400 14px/1.6 "Open Sans",sans-serif;color:var(--white)}
.contact-list li{display:flex;gap:18px;align-items:flex-start;margin-bottom:14px}
.contact-list svg{flex:none;margin-top:2px}
.links{position:absolute;left:490px;top:4068px;list-style:none;font:400 14px/26px "Open Sans",sans-serif;color:var(--white)}
.quote-lead{position:absolute;left:702px;top:4064px;font:400 14px "Open Sans",sans-serif;color:var(--white)}
.field{position:absolute;height:38px;border:1px solid #8a8ca0;padding:0 12px;display:flex;align-items:center;font:400 12px "Open Sans",sans-serif;color:var(--white)}
.submit{position:absolute;left:702px;top:4212px;width:210px;height:38px;background:var(--red);color:var(--white);font:700 16px "Roboto",sans-serif;display:flex;align-items:center;justify-content:center}
.copyright{position:absolute;left:0;top:4374px;width:1200px;text-align:center;font:400 14px "Open Sans",sans-serif;color:var(--white)}
</style>
</head>
<body>
<div class="page">

  <!-- hero -->
  <header class="hero">
    <svg class="hero-photo" width="1200" height="780" viewBox="0 0 1200 780">
      <defs>
        <linearGradient id="heroGrad" x1="0" y1="0" x2="1" y2="0.6">
          <stop offset="0" stop-color="#0d2b55"/>
          <stop offset="0.35" stop-color="#1a8fd6"/>
          <stop offset="0.6" stop-color="#0b2740"/>
          <stop offset="1" stop-color="#060b14"/>
        </linearGradient>
      </defs>
      <rect role="img" aria-label="Photo of glowing blue fibre optic cables" width="1200" height="780" fill="url(#heroGrad)"/>
      <polygon points="0,606 600,745 1200,606 1200,780 0,780" fill="var(--red)"/>
      <polygon points="0,606 600,745 1200,606 1200,780 0,780" fill="var(--white)" transform="translate(0,28)"/>
      <polygon points="500,0 1200,0 1200,36 520,36" fill="var(--red)"/>
    </svg>
    <div class="topbar-info">
      <span><svg width="14" height="14" viewBox="0 0 24 24"><path d="M6 2l4 4-2.5 3a13 13 0 0 0 7.5 7.5L18 14l4 4-3 4C10 21 3 14 2 5z" fill="#fff"/></svg>CALL 968 4410 2750</span>
      <span><svg width="16" height="12" viewBox="0 0 16 12"><rect width="16" height="12" fill="#fff"/><path d="M0 0l8 6 8-6" stroke="#c8161d" stroke-width="1.5" fill="none"/></svg>info@beitkarim.com</span>
      <span class="socials"><i></i><i></i><i></i><i></i></span>
    </div>
    <div class="logo"><span class="logo-mark"></span><span class="logo-name">BEIT KARIM</span></div>
    <nav class="nav"><span>HOME</span><span>ABOUT</span><span>OUR SOLUTIONS</span><span>OUR SERVICES</span><span>BLOG</span><span>CONTACT US</span></nav>
    <h1 class="hero-title">CABLING SUPPLY<br>AND SERVICE</h1>
    <p class="hero-sub">Sed ut perspiciatis unde omnis iste natus<br>error sit voluptatem accusantium</p>
    <div class="btn-red">GET MORE INFO</div>
    <div class="dots"><i class="on"></i><i></i><i></i><i></i></div>
  </header>

  <!-- services -->
  <h2 class="section-title" style="top:850px">OUR <b>SERVICES</b></h2>
  <div class="rule" style="top:916px"></div>

  <div class="service" style="left:117px;top:988px">
    <svg class="service-icon" width="112" height="112" viewBox="0 0 112 112"><circle cx="56" cy="56" r="54" fill="none" stroke="#d0d0d0" stroke-width="2"/><circle cx="56" cy="56" r="46" fill="var(--red)"/><rect x="36" y="40" width="40" height="28" rx="2" fill="none" stroke="#fff" stroke-width="3"/><path d="M52 48l10 6-10 6z" fill="#fff"/><path d="M46 74h20" stroke="#fff" stroke-width="3"/></svg>
    <h3>VIDEO WALL SYSTEM SUPPLY</h3>
    <p>Sed ut perspiciatis unde omnis iste natus<br>error sit voluptatem accusantium dolorque<br>laudantium, totam rem aperiam</p>
  </div>
  <div class="service" style="left:450px;top:988px">
    <svg class="service-icon" width="112" height="112" viewBox="0 0 112 112"><circle cx="56" cy="56" r="54" fill="none" stroke="#d0d0d0" stroke-width="2"/><circle cx="56" cy="56" r="46" fill="var(--red)"/><rect x="38" y="42" width="32" height="16" rx="3" fill="#fff"/><path d="M70 48l8-4v12l-8-4" fill="#fff"/><path d="M50 58v14h-8" stroke="#fff" stroke-width="3" fill="none"/></svg>
    <h3>CCTV SERVICE</h3>
    <p>Sed ut perspiciatis unde omnis iste natus<br>error sit voluptatem accusantium dolorque<br>laudantium, totam rem aperiam</p>
  </div>
  <div class="service" style="left:783px;top:988px">
    <svg class="service-icon" width="112" height="112" viewBox="0 0 112 112"><circle cx="56" cy="56" r="54" fill="none" stroke="#d0d0d0" stroke-width="2"/><circle cx="56" cy="56" r="46" fill="var(--red)"/><rect x="38" y="36" width="14" height="40" fill="none" stroke="#fff" stroke-width="3"/><rect x="60" y="36" width="14" height="40" fill="none" stroke="#fff" stroke-width="3"/><path d="M52 50l8 12M60 50l-8 12" stroke="#fff" stroke-width="3"/></svg>
    <h3>ACCESS CONTROL</h3>
    <p>Sed ut perspiciatis unde omnis iste natus<br>error sit voluptatem accusantium dolorque<br>laudantium, totam rem aperiam</p>
  </div>
  <div class="service" style="left:117px;top:1268px">
    <svg class="service-icon" width="112" height="112" viewBox="0 0 112 112"><circle cx="56" cy="56" r="54" fill="none" stroke="#d0d0d0" stroke-width="2"/><circle cx="56" cy="56" r="46" fill="var(--red)"/><circle cx="56" cy="56" r="8" fill="none" stroke="#fff" stroke-width="3"/><circle cx="56" cy="56" r="16" fill="none" stroke="#fff" stroke-width="3"/><circle cx="56" cy="56" r="24" fill="none" stroke="#fff" stroke-width="3" stroke-dasharray="30 8"/></svg>
    <h3>BIO METRIC SYSTEM</h3>
    <p>Sed ut perspiciatis unde omnis iste natus<br>error sit voluptatem accusantium dolorque<br>laudantium, totam rem aperiam</p>
  </div>
  <div class="service" style="left:450px;top:1268px">
    <svg class="service-icon" width="112" height="112" viewBox="0 0 112 112"><circle cx="56" cy="56" r="54" fill="none" stroke="#d0d0d0" stroke-width="2"/><circle cx="56" cy="56" r="46" fill="var(--red)"/><rect x="34" y="38" width="44" height="30" rx="2" fill="none" stroke="#fff" stroke-width="3"/><path d="M46 48l-6 5 6 5M66 48l6 5-6 5" stroke="#fff" stroke-width="3" fill="none"/><path d="M44 76h24" stroke="#fff" stroke-width="3"/></svg>
    <h3>IT SOFTWARE</h3>
    <p>Sed ut perspiciatis unde omnis iste natus<br>error sit voluptatem accusantium dolorque<br>laudantium, totam rem aperiam</p>
  </div>
  <div class="service" style="left:783px;top:1268px">
    <svg class="service-icon" width="112" height="112" viewBox="0 0 112 112"><circle cx="56" cy="56" r="54" fill="none" stroke="#d0d0d0" stroke-width="2"/><circle cx="56" cy="56" r="46" fill="var(--red)"/><rect x="34" y="36" width="36" height="28" rx="2" fill="none" stroke="#fff" stroke-width="3"/><rect x="64" y="52" width="16" height="24" rx="2" fill="#fff"/><path d="M40 72h22" stroke="#fff" stroke-width="3"/></svg>
    <h3>HARDWARE SUPPLY</h3>
    <p>Sed ut perspiciatis unde omnis iste natus<br>error sit voluptatem accusantium dolorque<br>laudantium, totam rem aperiam</p>
  </div>

  <!-- solutions band -->
  <section class="band">
    <svg width="1200" height="436" viewBox="0 0 1200 436">
      <defs>
        <linearGradient id="bandA" x1="0" y1="0" x2="1" y2="1"><stop offset="0" stop-color="#2a6fb8"/><stop offset="1" stop-color="#0c1f4a"/></linearGradient>
        <linearGradient id="bandB" x1="0" y1="0" x2="1" y2="1"><stop offset="0" stop-color="#5a4a3a"/><stop offset="1" stop-color="#1e2633"/></linearGradient>
        <linearGradient id="bandC" x1="0" y1="0" x2="1" y2="1"><stop offset="0" stop-color="#3a5a8a"/><stop offset="0.5" stop-color="#b8202a"/><stop offset="1" stop-color="#1a2540"/></linearGradient>
      </defs>
      <polygon role="img" aria-label="Photo of blue data cabling" points="0,0 460,0 425,436 0,436" fill="url(#bandA)"/>
      <polygon role="img" aria-label="Photo of a technician at a building management screen" points="460,0 790,0 755,436 425,436" fill="url(#bandB)"/>
      <polygon role="img" aria-label="Photo of a red fire alarm bell" points="790,0 1200,0 1200,436 755,436" fill="url(#bandC)"/>
      <rect width="1200" height="436" fill="#0c1633" opacity=".25"/>
      <path d="M460 0L425 436M790 0L755 436" stroke="#d8dde6" stroke-width="6"/>
    </svg>
    <div class="band-label" style="left:113px;top:184px">CABLING SUPPLY<br>&amp; SERVICE</div>
    <div class="band-label" style="left:443px;top:184px">BMS SUPPLY<br>AND SERVICE</div>
    <div class="band-label" style="left:767px;top:184px">FIRE AND SAFETY<br>SUPPLY &amp; SERVICE</div>
  </section>

  <!-- welcome -->
  <section class="welcome">
    <svg class="welcome-photo" width="640" height="576" viewBox="0 0 640 576">
      <defs><linearGradient id="welcomeGrad" x1="0" y1="0" x2="1" y2="0"><stop offset="0" stop-color="#eef0f2"/><stop offset="0.35" stop-color="#c9c5c0"/><stop offset="1" stop-color="#8a8580"/></linearGradient></defs>
      <rect role="img" aria-label="Photo of two colleagues working at a computer in an office" width="640" height="576" fill="url(#welcomeGrad)"/>
    </svg>
    <h2>WELCOME TO <span>BEIT KARIM</span></h2>
    <p>Sed ut perspiciatis unde omnis iste natus error sit voluptatem accusium doloremque laudantium, totam rem aperiam, eaque ipsa quae ab illo inventore veritatis et quasi architecto beatae vitae dicta sunt explicabo. Nemo enim ipsam voluptatem quia voluptas sit aspernatur aut odit aut fugit, sed quia consequuntur magni dolores eos Nemo enim ipsam voluptatem</p>
    <div class="btn-outline">READ MORE</div>
  </section>

  <!-- news -->
  <h2 class="section-title" style="top:2708px"><b>LATEST</b> NEWS</h2>
  <div class="rule" style="top:2782px"></div>

  <article class="news-card" style="left:136px;top:2826px">
    <svg class="news-photo" viewBox="0 0 288 184"><defs><linearGradient id="n1" x1="0" y1="0" x2="1" y2="1"><stop offset="0" stop-color="#d8206a"/><stop offset=".5" stop-color="#3a7ad8"/><stop offset="1" stop-color="#e8a020"/></linearGradient></defs><rect role="img" aria-label="Photo of colourful network cables" width="288" height="184" fill="url(#n1)"/></svg>
    <h4>Quis autem vel eum iure</h4>
    <div class="news-date"><svg width="11" height="11" viewBox="0 0 11 11"><rect y="1" width="11" height="10" fill="#c8161d"/><rect x="1.5" y="4" width="8" height="5.5" fill="#fff"/></svg>OCTOBER 17, 2019</div>
    <p>Sed ut perspiciatis unde omnis iste natus error sit voluptatem accusantium dolorque lalum, totam rem aperiam</p>
  </article>
  <article class="news-card" style="left:456px;top:2850px">
    <svg class="news-photo" viewBox="0 0 288 184"><defs><linearGradient id="n2" x1="0" y1="0" x2="1" y2="1"><stop offset="0" stop-color="#dfe8f4"/><stop offset=".6" stop-color="#7fa0cf"/><stop offset="1" stop-color="#2c3b66"/></linearGradient></defs><rect role="img" aria-label="Photo of a security camera with network graphics" width="288" height="184" fill="url(#n2)"/></svg>
    <h4>Quis autem vel eum iure</h4>
    <div class="news-date"><svg width="11" height="11" viewBox="0 0 11 11"><rect y="1" width="11" height="10" fill="#c8161d"/><rect x="1.5" y="4" width="8" height="5.5" fill="#fff"/></svg>OCTOBER 17, 2019</div>
    <p>Sed ut perspiciatis unde omnis iste natus error sit voluptatem accusantium dolorque lalum, totam rem aperiam</p>
  </article>
  <article class="news-card" style="left:776px;top:2826px">
    <svg class="news-photo" viewBox="0 0 288 184"><defs><linearGradient id="n3" x1="0" y1="0" x2="1" y2="1"><stop offset="0" stop-color="#9aa3ab"/><stop offset="1" stop-color="#3b444d"/></linearGradient></defs><rect role="img" aria-label="Photo of a team meeting in an office" width="288" height="184" fill="url(#n3)"/></svg>
    <h4>Quis autem vel eum iure</h4>
    <div class="news-date"><svg width="11" height="11" viewBox="0 0 11 11"><rect y="1" width="11" height="10" fill="#c8161d"/><rect x="1.5" y="4" width="8" height="5.5" fill="#fff"/></svg>OCTOBER 17, 2019</div>
    <p>Sed ut perspiciatis unde omnis iste natus error sit voluptatem accusantium dolorque lalum, totam rem aperiam</p>
  </article>

  <!-- testimonials -->
  <section class="testimonials">
    <svg class="abs" style="left:0;top:0" width="1200" height="730" viewBox="0 0 1200 730">
      <defs><linearGradient id="tGrad" x1="0" y1="0" x2="1" y2="1"><stop offset="0" stop-color="#b8141b"/><stop offset=".5" stop-color="#d11b22"/><stop offset="1" stop-color="#a5111a"/></linearGradient></defs>
      <rect role="img" aria-label="Red tinted background photo" width="1200" height="730" fill="url(#tGrad)"/>
    </svg>
    <h2 class="section-title">TESTIMONIALS</h2>
    <div class="rule" style="top:134px;background:var(--white)"></div>
    <div class="quote-card" style="left:157px">
      <p>Sed ut perspiciatis unde omnis iste natus error sit voluptatem accusantium doloremque laudantium, totam rem aperiam, eaque ipsa quae ab illo inventore veritatis et quasi architecto beatae vitae</p>
      <div class="quote-name" style="left:26px">Omar Salem -<br>Beit Karim</div>
      <div class="quote-mark" style="left:200px">&rdquo;</div>
    </div>
    <div class="quote-card" style="left:634px">
      <p style="text-align:right">Sed ut perspiciatis unde omnis iste natus error sit voluptatem accusantium doloremque laudantium, totam rem aperiam, eaque ipsa quae ab illo inventore veritatis et quasi architecto beatae vitae dicta</p>
      <div class="quote-name" style="right:26px;text-align:right">Omar Salem -<br>Beit Karim</div>
      <div class="quote-mark" style="left:160px">&ldquo;</div>
    </div>
  </section>
  <div class="avatar" role="img" aria-label="Client portrait photo" style="left:462px"></div>
  <div class="avatar" role="img" aria-label="Client portrait photo" style="left:602px"></div>

  <!-- footer -->
  <footer>
    <svg class="abs" style="left:0;top:3840px" width="1200" height="604" viewBox="0 0 1200 604">
      <polygon points="0,130 600,0 1200,130 1200,604 0,604" fill="var(--navy)"/>
      <polyline points="0,130 600,0 1200,130" fill="none" stroke="var(--white)" stroke-width="8"/>
      <rect y="490" width="1200" height="114" fill="var(--navy-deep)"/>
      <line x1="0" y1="490" x2="1200" y2="490" stroke="#34364d" stroke-width="1"/>
    </svg>
    <h3 class="footer-title" style="left:172px">CONTACT US</h3>
    <ul class="contact-list">
      <li><svg width="14" height="18" viewBox="0 0 14 18"><path d="M7 0a7 7 0 0 0-7 7c0 5 7 11 7 11s7-6 7-11a7 7 0 0 0-7-7z" fill="#fff"/><circle cx="7" cy="7" r="2.5" fill="#1d1f35"/></svg><span>9 Qurum Street,<br>Muscat 112, Oman</span></li>
      <li><svg width="14" height="14" viewBox="0 0 24 24"><path d="M6 2l4 4-2.5 3a13 13 0 0 0 7.5 7.5L18 14l4 4-3 4C10 21 3 14 2 5z" fill="#fff"/></svg><span>Phone: +968 4410 2750</span></li>
      <li><svg width="14" height="14" viewBox="0 0 14 14"><rect x="1" y="5" width="12" height="8" fill="#fff"/><rect x="3" y="1" width="8" height="4" fill="none" stroke="#fff" stroke-width="1.5"/></svg><span>Fax: 0244 310 5120</span></li>
      <li><svg width="16" height="12" viewBox="0 0 16 12"><rect x=".75" y=".75" width="14.5" height="10.5" fill="none" stroke="#fff" stroke-width="1.5"/><path d="M1 1l7 6 7-6" stroke="#fff" stroke-width="1.5" fill="none"/></svg><span>Email: info@beitkarim.com</span></li>
    </ul>
    <h3 class="footer-title" style="left:490px">QUICK LINKS</h3>
    <ul class="links"><li>Home</li><li>About</li><li>Our Services</li><li>Blog</li><li>Team</li><li>Contac</li></ul>
    <h3 class="footer-title" style="left:702px">REQUEST A QUOTE</h3>
    <p class="quote-lead">Alternatively You Can Fill In The Following Contact Form:</p>
    <div class="field" style="left:702px;top:4104px;width:188px">Name</div>
    <div class="field" style="left:898px;top:4104px;width:188px">E - Mail</div>
    <div class="field" style="left:702px;top:4152px;width:188px">Subject</div>
    <div class="field" style="left:898px;top:4152px;width:188px">Message</div>
    <div class="submit">SUBMIT</div>
    <p class="copyright">(c) 2019 Beit Karim | All Rights Reserved | Terms and Conditions</p>
  </footer>

</div>
</body>
</html>
```